Elegant eBook Word Template Design Required

I need an ebook template designed to match my website branding. It needs to include index, intro, chapters and about me. Word format required.

I will be using this template to create downloadable pdfs on my website.

For branding visit my website http://ravelcoraston.com.au

Facebook: @RavelCorastonOnline

Target Market(s)

Business owners, Entrepreneurs

Industry/Entity Type

Business Consultant

Font styles to use
Other font styles liked:
• check website

Colors

Designer to choose colors to be used in the design.

Requirements
Must have
• - Font and colour scheme must match my website branding

```html
<!DOCTYPE html>
<html lang="en">
<head>
<meta charset="utf-8">
<title>Ravel Coraston – eBook Template</title>
<link href="https://fonts.googleapis.com/css2?family=Montserrat:wght@400;600;700;800&family=Raleway:wght@400;700&family=Didact+Gothic&display=swap" rel="stylesheet">
<style>
  :root {
    --brand-blue: #4aa3c2;
    --page-grey: #e8e9eb;
    --page-white: #ffffff;
    --ink: #2b2b2b;
    --ink-soft: #555a5e;
    --backdrop: #f2f0ec;
    --photo-dark: #3a3a3c;
    --photo-light: #c9ccd0;
  }
  * { margin: 0; padding: 0; box-sizing: border-box; }
  html, body { width: 800px; height: 1200px; overflow: hidden; }
  body { background: var(--backdrop); position: relative; font-family: "Didact Gothic", sans-serif; color: var(--ink-soft); }

  .page { position: absolute; width: 232px; height: 300px; overflow: hidden; box-shadow: 3px 4px 8px rgba(0,0,0,0.22); }
  .page--grey { background: var(--page-grey); }
  .page--white { background: var(--page-white); }
  .col-1 { left: 18px; } .col-2 { left: 288px; } .col-3 { left: 553px; }
  .row-1 { top: 86px; } .row-2 { top: 450px; } .row-3 { top: 815px; }

  .photo { position: absolute; }
  .brand-name { font-family: "Montserrat", sans-serif; font-weight: 700; color: var(--brand-blue); letter-spacing: 0.02em; }
  .next-button { position: absolute; width: 36px; height: 36px; }
  .body-copy { font-size: 8.5px; line-height: 1.18; letter-spacing: 0.08em; position: absolute; }
  .fine-print { font-size: 6px; line-height: 1.25; letter-spacing: 0.08em; position: absolute; }

  /* Cover */
  .cover .photo { inset: 0 22px 0 0; background: linear-gradient(135deg, #d9dde1 0%, #a9b0b8 45%, #3b4150 100%); }
  .cover__strip { position: absolute; top: 0; right: 0; width: 22px; height: 100%; background: var(--brand-blue); }
  .cover__title { position: absolute; left: 118px; top: 62px; width: 92px; text-align: center; }
  .cover__title .dot { display: block; width: 18px; height: 18px; border-radius: 50%; background: var(--brand-blue); margin: 0 auto 5px; }
  .cover__title .brand-name { color: #2b2b2b; font-size: 9.5px; }

  /* Intro quote */
  .intro { background: var(--page-grey); }
  .intro__band { position: absolute; inset: 0; }
  .intro__name { position: absolute; top: 36px; width: 100%; text-align: center; font-family: "Montserrat", sans-serif; font-weight: 800; color: #fff; font-size: 26px; line-height: 1; letter-spacing: -0.01em; }
  .intro__quote { position: absolute; top: 126px; left: 14px; right: 14px; text-align: center; font-family: "Raleway", sans-serif; color: #fff; font-size: 8.4px; line-height: 1.37; }
  .intro__quote strong { font-weight: 700; }

  /* About */
  .about .photo { left: 0; top: 0; width: 112px; height: 100%; background: linear-gradient(160deg, #4a3a32 0%, #2e2a2c 55%, #1f2330 100%); }
  .about__heading { position: absolute; left: 80px; top: 194px; transform: rotate(-90deg); transform-origin: left top; font-family: "Montserrat", sans-serif; font-weight: 700; color: #fff; font-size: 29px; letter-spacing: 0.06em; white-space: nowrap; line-height: 1; }
  .about__text { position: absolute; left: 124px; top: 42px; width: 98px; font-size: 8.6px; line-height: 1.17; letter-spacing: 0.09em; }
  .about__text p + p { margin-top: 10px; }

  /* Contents */
  .contents .photo { inset: 0; background: linear-gradient(135deg, #6c6f74 0%, #3e4146 50%, #24262a 100%); }
  .contents__hex { position: absolute; inset: 0; }
  .contents__title { position: absolute; left: 38px; top: 95px; font-family: "Montserrat", sans-serif; font-weight: 600; color: #fff; font-size: 13px; letter-spacing: 0.12em; }
  .contents__list { position: absolute; left: 38px; top: 126px; width: 156px; list-style: none; font-family: "Montserrat", sans-serif; font-weight: 600; color: #fff; font-size: 6.6px; letter-spacing: 0.06em; }
  .contents__list li { display: flex; margin-bottom: 10px; }
  .contents__list .leader { flex: 1; border-bottom: 1px dotted #fff; margin: 0 2px 2px; }

  /* Chapter */
  .chapter__title { position: absolute; left: 14px; top: 22px; font-family: "Montserrat", sans-serif; font-weight: 600; color: var(--ink); font-size: 15px; letter-spacing: 0.1em; }
  .chapter__brand { position: absolute; right: 14px; top: 26px; font-size: 7px; display: flex; align-items: center; gap: 3px; }
  .chapter__brand .square { width: 7px; height: 7px; background: var(--brand-blue); }
  .chapter__intro { left: 14px; top: 54px; width: 160px; }
  .chapter__dots { position: absolute; left: 24px; top: 142px; width: 186px; display: flex; justify-content: space-between; }
  .chapter__dots span { width: 40px; height: 40px; border-radius: 50%; background: var(--brand-blue); }
  .chapter__body { right: 18px; top: 238px; width: 200px; text-align: right; }

  /* Callout */
  .callout__intro { left: 20px; top: 20px; width: 196px; }
  .callout__hex { position: absolute; left: 46px; top: 102px; width: 138px; height: 154px; }
  .callout__text { position: absolute; left: 60px; top: 166px; width: 110px; text-align: center; color: #fff; font-size: 7.6px; line-height: 1.3; letter-spacing: 0.1em; }

  /* Text pages */
  .text-page__para { left: 16px; width: 200px; text-align: center; }
  .closing__para { right: 18px; width: 200px; text-align: right; }
  .closing__para--bold { font-family: "Montserrat", sans-serif; font-weight: 700; color: var(--ink); font-size: 7.4px; letter-spacing: 0.12em; }
  .closing__house { position: absolute; left: 0; top: 0; width: 232px; height: 300px; }
  .closing__name { position: absolute; left: 14px; top: 226px; width: 130px; font-family: "Montserrat", sans-serif; font-weight: 800; color: #fff; font-size: 24px; line-height: 1.02; }

  /* Back cover */
  .back__brand { position: absolute; top: 136px; width: 100%; display: flex; justify-content: center; align-items: center; gap: 6px; font-size: 14px; }
  .back__brand .square { width: 12px; height: 12px; background: var(--brand-blue); }
</style>
</head>
<body>

<!-- Row 1 -->
<section class="page cover col-1 row-1">
  <div class="photo" role="img" aria-label="Photo of the consultant presenting to an audience"></div>
  <div class="cover__strip"></div>
  <div class="cover__title"><span class="dot"></span><span class="brand-name">RAVEL CORASTON</span></div>
</section>

<section class="page intro col-2 row-1">
  <svg class="intro__band" viewBox="0 0 232 300" aria-hidden="true"><path d="M0 0H232V178L124 232Q116 236 108 232L0 178Z" fill="var(--brand-blue)"/></svg>
  <div class="intro__name">Ravel<br>Coraston</div>
  <p class="intro__quote">“Having delivered breakthrough results to clients of various professional and personal backgrounds, I know <strong>what works</strong>, and <strong>more importantly</strong>,<br>I know how to uncover what<br><strong>WILL WORK FOR YOU!”</strong></p>
  <svg class="next-button" style="left:99px;top:246px" viewBox="0 0 36 36" aria-label="Next"><circle cx="18" cy="18" r="17" fill="var(--brand-blue)"/><path d="M15 10l8 8-8 8" stroke="#fff" stroke-width="3" fill="none" stroke-linecap="round"/></svg>
</section>

<section class="page page--grey about col-3 row-1">
  <div class="photo" role="img" aria-label="Portrait photo of the consultant seated"></div>
  <h2 class="about__heading">ABOUT ME</h2>
  <div class="about__text">
    <p>Thanks for taking the chance to get to know me better.</p>
    <p>I'd love to give you my full life story, but I decided that would be dull. Instead, I want to share with you stories of simple principles I have learnt, that will help you improve your life ten-fold!</p>
    <p>Let's get started...</p>
  </div>
  <svg class="next-button" style="left:151px;top:259px;width:30px;height:30px" viewBox="0 0 36 36" aria-label="Next"><circle cx="18" cy="18" r="17" fill="var(--brand-blue)"/><path d="M15 10l8 8-8 8" stroke="#fff" stroke-width="3" fill="none" stroke-linecap="round"/></svg>
</section>

<!-- Row 2 -->
<section class="page contents col-1 row-2">
  <div class="photo" role="img" aria-label="Photo of the consultant speaking with hands raised"></div>
  <svg class="contents__hex" viewBox="0 0 232 300" aria-hidden="true"><polygon points="114,44 212,98 212,210 114,264 18,210 18,98" fill="rgba(255,255,255,0.2)"/></svg>
  <h2 class="contents__title">TABLE OF CONTENT</h2>
  <ol class="contents__list">
    <li>CHAPTER 1<span class="leader"></span>6</li>
    <li>CHAPTER 2<span class="leader"></span>10</li>
    <li>CHAPTER 3<span class="leader"></span>15</li>
  </ol>
</section>

<section class="page page--white chapter col-2 row-2">
  <h2 class="chapter__title">chapter 1</h2>
  <div class="chapter__brand"><span class="square"></span><span class="brand-name">Ravel Coraston</span></div>
  <p class="fine-print chapter__intro">Lorem ipsum dolor sit amet, consectetur adipiscing elit. Praesent quis tempus turpis. Sed at varius orci. Duis accumsan finibus fringilla. Integer maximus porttitor ligula nec consequat.</p>
  <div class="chapter__dots"><span></span><span></span><span></span></div>
  <p class="body-copy chapter__body">Lorem ipsum dolor sit amet, consectetur adipiscing elit. Praesent quis tempus turpis. Sed at varius orci. Duis accumsan finibus fringilla. Integer maximus porttitor ligula nec consequat.</p>
</section>

<section class="page page--grey callout col-3 row-2">
  <p class="fine-print callout__intro">Lorem ipsum dolor sit amet, consectetur adipiscing elit. Praesent quis tempus turpis. Sed at varius orci. Duis accumsan finibus fringilla. Integer maximus porttitor ligula nec consequat.</p>
  <svg class="callout__hex" viewBox="0 0 138 154" aria-hidden="true"><path d="M62 3Q69 0 76 3L130 34Q137 38 137 46V108Q137 116 130 120L76 151Q69 154 62 151L8 120Q1 116 1 108V46Q1 38 8 34Z" fill="var(--brand-blue)"/></svg>
  <p class="callout__text">Lorem ipsum dolor sit amet, consectetur adipiscing elit.</p>
</section>

<!-- Row 3 -->
<section class="page page--grey text-page col-1 row-3">
  <p class="body-copy text-page__para" style="top:81px">Lorem ipsum dolor sit amet, consectetur adipiscing elit. Praesent quis tempus turpis. Sed at varius orci. Duis accumsan finibus fringilla. Integer maximus porttitor ligula nec consequat.</p>
  <p class="body-copy text-page__para" style="top:169px">Lorem ipsum dolor sit amet, consectetur adipiscing elit. Praesent quis tempus turpis. Sed at varius orci. Duis accumsan finibus fringilla. Integer maximus porttitor ligula nec consequat.</p>
</section>

<section class="page page--white closing col-2 row-3">
  <p class="body-copy closing__para" style="top:18px">Lorem ipsum dolor sit amet, consectetur adipiscing elit. Praesent quis tempus turpis. Sed at varius orci. Duis accumsan finibus fringilla. Integer maximus porttitor ligula nec consequat.</p>
  <p class="body-copy closing__para closing__para--bold" style="top:106px">Lorem ipsum dolor sit amet, consectetur adipiscing elit. Praesent quis tempus turpis. Sed at varius orci.</p>
  <svg class="closing__house" viewBox="0 0 232 300" aria-hidden="true"><path d="M0 182L72 146Q80 142 88 146L160 182Q170 188 170 198V300H0Z" fill="var(--brand-blue)"/></svg>
  <div class="closing__name">Ravel<br>Coraston</div>
</section>

<section class="page page--grey back col-3 row-3">
  <div class="back__brand"><span class="square"></span><span class="brand-name">Ravel Coraston</span></div>
</section>

</body>
</html>
```